Jewellery retailer needs a flyer design please

We need a flyer to represent our business.

Our company provides The lowest priced diamonds in Australia.
We are wholesales who sell direct to the public
We GENUINELY are 50-70% cheaper than other retail stores.

We guarantee the lowest prices, even in the unlikely event a customer finds a cheaper price than ours, we will beat it too.

Well tell our customers if youre not buying from us then you're paying too much.

Please include website www.amberloomstore.com.au
and facebook page www.facebook.com/mosslightcove.

We have location in Harbourgate Parramatta, and Harbourgate Liverpool, NSW.

Im sorry, this is the first time ive done this, so i hope ive given the information you need.

Target Market(s)

People wanting to buy engagement rings are our biggest customers.

Industry/Entity Type

Retail

Colors
276db0
3276b5
86acd3
cedeed

Requirements
Must have
• Simple, to the point! We need people to know that we have the lowest prices without compromising on quality
Nice to have
• I am very very open to anything. I do not have any particular expectations

```html
<!DOCTYPE html>
<html lang="en">
<head>
<meta charset="utf-8">
<title>Amber Loom – Diamond Flyer</title>
<link rel="stylesheet" href="https://fonts.googleapis.com/css2?family=Questrial&display=swap">
<style>
  :root {
    --page-bg: #e6e6e6;
    --photo-dark: #4f4b4c;
    --photo-mid: #8d898a;
    --photo-light: #b9b6b7;
    --ink: #333132;
    --ink-soft: #3f3d3e;
    --white: #ffffff;
    --panel: rgba(255, 255, 255, 0.78);
    --panel-soft: rgba(255, 255, 255, 0.62);
    --badge-border: #2c2a2b;
    --logo-blue: #276db0;
  }
  * { margin: 0; padding: 0; box-sizing: border-box; }
  html, body {
    width: 1139px;
    height: 1200px;
    overflow: hidden;
    background: var(--page-bg);
    font-family: "Questrial", "Century Gothic", sans-serif;
  }
  .flyer {
    position: absolute;
    left: 169px;
    top: 31px;
    width: 800px;
    height: 1138px;
    overflow: hidden;
    box-shadow: 0 6px 24px rgba(0, 0, 0, 0.35);
  }
  .ring-photo {
    position: absolute;
    inset: 0;
    background:
      radial-gradient(ellipse 42% 30% at 30% 20%, rgba(235, 235, 238, 0.75), rgba(235, 235, 238, 0) 70%),
      radial-gradient(ellipse 60% 40% at 55% 62%, rgba(200, 198, 199, 0.55), rgba(200, 198, 199, 0) 75%),
      linear-gradient(170deg, var(--photo-dark) 0%, var(--photo-mid) 38%, var(--photo-light) 65%, var(--photo-mid) 100%);
  }
  .badges {
    position: absolute;
    top: 38px;
    left: 477px;
    display: flex;
    gap: 15px;
  }
  .badge {
    width: 136px;
    height: 117px;
    background: var(--white);
    border: 3px solid var(--badge-border);
    border-radius: 12px;
    display: flex;
    align-items: center;
    justify-content: center;
    text-align: center;
    font-size: 21px;
    line-height: 1.08;
    color: #111;
  }
  .headline {
    position: absolute;
    right: 40px;
    top: 222px;
    text-align: right;
    color: var(--white);
    font-size: 37px;
    line-height: 45px;
  }
  .guarantee {
    position: absolute;
    left: 43px;
    top: 555px;
    width: 510px;
    padding: 10px 16px;
    background: var(--panel-soft);
    border-radius: 14px;
    color: var(--ink);
    font-size: 27px;
    line-height: 34px;
    text-align: justify;
  }
  .savings {
    position: absolute;
    left: 395px;
    width: 400px;
    top: 690px;
    text-align: center;
    color: var(--ink-soft);
  }
  .savings .we { font-size: 40px; line-height: 58px; }
  .savings .genuinely { font-size: 50px; line-height: 62px; letter-spacing: 1px; }
  .savings .are { font-size: 33px; line-height: 52px; }
  .savings .percent { font-size: 47px; line-height: 62px; }
  .savings .compare { font-size: 40px; line-height: 52px; }
  .brand-card {
    position: absolute;
    left: 47px;
    top: 780px;
    width: 353px;
    height: 162px;
    background: var(--white);
    border: 3px solid #bdbbbc;
    display: flex;
    align-items: center;
    justify-content: center;
    gap: 14px;
  }
  .brand-mark {
    width: 26px;
    height: 26px;
    border-radius: 50%;
    background: var(--logo-blue);
  }
  .brand-name {
    font-size: 46px;
    color: var(--logo-blue);
  }
  .locations {
    position: absolute;
    left: 30px;
    top: 1012px;
    width: 303px;
    padding: 8px 12px;
    background: var(--panel);
    color: var(--ink);
    font-size: 21px;
    line-height: 25px;
  }
  .locations h2 {
    font-size: 20px;
    font-weight: 700;
    line-height: 25px;
  }
  .links {
    position: absolute;
    left: 392px;
    top: 1038px;
    width: 408px;
    padding: 7px 12px;
    background: var(--panel);
    color: var(--ink);
    font-size: 20px;
    line-height: 25px;
  }
</style>
</head>
<body>
  <main class="flyer">
    <div class="ring-photo" role="img" aria-label="Close-up photograph of a solitaire diamond engagement ring in a six-claw setting"></div>

    <div class="badges">
      <div class="badge">Lowest<br>Priced<br>Diamonds<br>in Australia</div>
      <div class="badge">Wholesalers<br>who sell<br>direct to<br>the public</div>
    </div>

    <h1 class="headline" style="font-weight:400">If you're<br>not buying<br>from us then<br>you're paying<br>too much.</h1>

    <p class="guarantee">We guarantee the lowest prices, even in the unlikely event a customer finds a cheaper price than ours, we will beat it too.</p>

    <div class="savings">
      <div class="we">We</div>
      <div class="genuinely">GENUINELY</div>
      <div class="are">are</div>
      <div class="percent">50-70%</div>
      <div class="compare">cheaper than<br>other retail stores</div>
    </div>

    <div class="brand-card">
      <span class="brand-mark"></span>
      <span class="brand-name">Amber Loom</span>
    </div>

    <section class="locations">
      <h2>Our Locations</h2>
      <p>Harbourgate Parramatta, NSW<br>Harbourgate Liverpool, NSW</p>
    </section>

    <div class="links">
      <p>www.amberloomstore.com.au</p>
      <p>www.facebook.com/mosslightcove</p>
    </div>
  </main>
</body>
</html>
```